Label design

Description
I want you to design a label for a skin care product line. I’ve provide the picture of the jar we are using along with the logo. Please note that the logo is available in different colors as well. (See attached) I would like the label to be very clean and straight to the point. Here is some info that I would like to see on the label:
240G
Net wt 8.0z

The content of the jar can be refer to as:

Body cream
Crème de corps
Body butter
Fade cream
Skin tone cream
Lotion pour le corps
Clarifying Body cream
Lightening Cream

The content is also made an exotic component that: “Extraits de noisette de palmiers” meaning nuts extract.

The brand NAME is: Mibaru
The tag line is: Be yourself, love yourself

Industry/Entity Type

Skin Care Product

```html
<!DOCTYPE html>
<html lang="fr">
<head>
<meta charset="utf-8">
<title>Mibaru – Clarifying Body Cream Label</title>
<link href="https://fonts.googleapis.com/css2?family=Source+Sans+3:wght@300;400;600&display=swap" rel="stylesheet">
<style>
  :root {
    --label-bg: #ffffff;
    --brand-orange: #f7941d;
    --brand-name: #f08a24;
    --mark-orange: #f5a023;
    --motif-yellow: #f8f3b6;
    --motif-fade: rgba(248, 243, 182, 0);
    --text-grey: #5f5f63;
    --text-white: #ffffff;
  }

  html, body {
    margin: 0;
    padding: 0;
    overflow: hidden;
    background: var(--label-bg);
  }

  .label {
    position: relative;
    width: 1200px;
    height: 475px;
    background: var(--label-bg);
    overflow: hidden;
    font-family: "Source Sans 3", "Helvetica Neue", Arial, sans-serif;
  }

  .motif {
    position: absolute;
    top: 60px;
    width: 360px;
    height: 415px;
    border-radius: 50%;
    background: radial-gradient(ellipse at 50% 50%, var(--motif-yellow) 0%, var(--motif-yellow) 45%, var(--motif-fade) 72%);
  }

  .motif-left { left: 80px; }
  .motif-right { left: 740px; }

  .brand {
    position: absolute;
    top: 30px;
    left: 0;
    width: 100%;
    text-align: center;
  }

  .brand-mark {
    display: block;
    width: 96px;
    height: 96px;
    margin: 0 auto;
    border-radius: 50%;
    background: var(--mark-orange);
  }

  .brand-name {
    margin: 6px 0 0;
    font-size: 80px;
    font-weight: 300;
    line-height: 1;
    letter-spacing: 1px;
    color: var(--brand-name);
  }

  .brand-tagline {
    margin: 6px 0 0;
    font-size: 17px;
    font-weight: 400;
    color: var(--text-grey);
  }

  .product-band {
    position: absolute;
    top: 284px;
    left: 0;
    width: 100%;
    height: 81px;
    background: var(--brand-orange);
    display: flex;
    align-items: center;
    justify-content: center;
  }

  .product-name {
    margin: 0;
    font-size: 37px;
    font-weight: 400;
    color: var(--text-white);
    letter-spacing: 0.3px;
  }

  .ingredient {
    position: absolute;
    top: 374px;
    left: 0;
    width: 100%;
    margin: 0;
    text-align: center;
    font-size: 17px;
    font-weight: 400;
    color: var(--text-grey);
  }

  .net-weight {
    position: absolute;
    top: 418px;
    left: 0;
    width: 100%;
    margin: 0;
    text-align: center;
    font-size: 27px;
    font-weight: 400;
    color: var(--text-grey);
  }

  .net-weight .divider {
    color: var(--brand-orange);
    font-weight: 600;
    padding: 0 5px;
  }
</style>
</head>
<body>
  <main class="label">
    <div class="motif motif-left" role="img" aria-label="Soft pale yellow decorative brand motif"></div>
    <div class="motif motif-right" role="img" aria-label="Soft pale yellow decorative brand motif"></div>

    <header class="brand">
      <span class="brand-mark" aria-hidden="true"></span>
      <h1 class="brand-name">Mibaru</h1>
      <p class="brand-tagline">Be yourself, love yourself</p>
    </header>

    <section class="product-band">
      <h2 class="product-name">Clarifying Body Cream</h2>
    </section>

    <p class="ingredient">Extraits de noisette de palmiers</p>

    <p class="net-weight">240g<span class="divider">|</span>Net wt 8.0z</p>
  </main>
</body>
</html>
```